Dr. Lumora needs a design for its website!

*Only need the design, coding is not required.
*Need desktop version ($500) and mobile/tablet version ($200)
*The attached files are not the exact layout we want, they are just for you to know what information should be included in those pages.
*The function of our website is like www.qavlo.hk
*For the background picture, prefer a lively picture and chinese people in it, NOT necessarily need a doctor or sick person in the picture

***Don't just copy the layout from the attachments or from the reference website, we are looking for creative ideas, non-ordinary designs!!!****

We are developing a website for the public to search a doctor by different criteria. At the initial stage, we need 4 pages to start with and other pages at later stage. I have attached the general idea of these pages but not necessarily to be exactly the same, I am looking for some new ideas.

This website needs a professional, modern, simple and user friendly design. The main color to be used in the website will be same as the color (R:0 G:139 B:205) used in our logo (see attached). We don't have any particular thoughts for the other color and the font to be used in the website. Can try to use circle outline for the icon in the navigation bar.

1. Home: will include 4 sections (see attached)

2. Doctor's details (see attached)

3. Health information: will include a short descriptions of this Health Info page and 5 sections (see attached)

4. News (see attached)

Reason: Not too many suitable designs to choose from and need more time to go through the designs

All

Medical

4 page

• must not be same as or looks too much like www.qavlo.hk
• prefer not to use black and red color

```html
<!DOCTYPE html>
<html lang="en">
<head>
<meta charset="utf-8">
<title>Dr. Lumora</title>
<link href="https://fonts.googleapis.com/css2?family=Open+Sans:wght@400;600;700;800&family=Noto+Sans+SC:wght@400&display=swap" rel="stylesheet">
<style>
:root{
  --blue:#0a8bcd;
  --blue-dark:#0b5d8c;
  --navy:#0c2f4a;
  --ink:#333;
  --text:#444;
  --light:#f2f2f2;
  --row:#ebebeb;
  --footer:#1f1f1f;
  --footer-field:#3a3a3a;
  --pink:#e8506e;
}
*{box-sizing:border-box;margin:0;padding:0}
html,body{width:814px;height:1200px;overflow:hidden}
body{background:#e6e6e6;font-family:"Open Sans",Arial,sans-serif;color:var(--ink);position:relative}
.abs{position:absolute}
.page{position:absolute;left:10px;top:10px;width:794px;height:1182px;background:#fff;overflow:hidden}
/* header */
.brand{left:20px;top:12px;display:flex;align-items:center;gap:8px}
.brand-dot{width:46px;height:46px;border-radius:50%;background:var(--blue)}
.brand-name{font-size:28px;font-weight:400;color:var(--blue);letter-spacing:-.5px}
.lang{right:20px;top:8px;font-size:9px;color:#555;font-family:"Open Sans","Noto Sans SC",sans-serif}
.member-note{left:470px;top:40px;font-size:7px;font-weight:700;color:#444}
.forgot{right:21px;top:40px;font-size:7px;font-weight:700;color:#444}
.field-top{top:54px;height:20px;background:#f1f1f1;border:1px solid #ccc;border-radius:3px;font-size:8.5px;font-weight:600;color:#333;display:flex;align-items:center;justify-content:center}
.btn-login{left:685px;top:54px;width:88px;height:20px;background:linear-gradient(#1591d4,#0b5d8c);color:#fff;font-size:10px;font-weight:700;border-radius:3px;display:flex;align-items:center;justify-content:center}
/* nav */
.nav{left:0;top:88px;width:794px;height:34px;background:var(--blue)}
.nav-item{top:0;height:34px;display:flex;align-items:center;justify-content:center;color:#fff;font-size:10.5px;font-weight:700}
.nav-home{background:var(--blue-dark)}
.nav-sep{top:0;width:1px;height:34px;background:rgba(255,255,255,.35)}
.nav-search{left:543px;top:8px;width:170px;height:19px;background:#fff;border-radius:10px;display:flex;align-items:center;gap:5px;padding-left:8px;font-size:9px;font-weight:700;color:#222}
/* member */
.section-title{font-size:17px;font-weight:700;color:#333;display:flex;align-items:center;gap:8px;white-space:nowrap}
.perk{width:140px;text-align:center;font-size:9px;font-weight:600;color:#333;line-height:14px}
.perk-ring{width:84px;height:84px;border-radius:50%;border:1px solid #ddd;margin:0 auto 6px;display:flex;align-items:center;justify-content:center}
.perk-disc{width:76px;height:76px;border-radius:50%;background:var(--blue);display:flex;align-items:center;justify-content:center}
/* finder */
.finder{left:0;top:376px;width:794px;height:252px;background:linear-gradient(135deg,#2c86c4,#1b78b8 45%,#3a93cf);}
.finder-title{left:0;top:44px;width:794px;justify-content:center;color:#fff;font-size:17px;font-weight:700}
.f-label{font-size:9.5px;font-weight:700;color:#fff}
.f-input{height:20px;background:#fff;border-radius:3px;border:1px solid #d6d6d6}
.f-select{display:flex;align-items:center;justify-content:flex-end;padding-right:7px}
.check{display:flex;align-items:center;gap:5px;font-size:9.5px;font-weight:600;color:#fff}
.check i{display:block;width:8px;height:8px;background:#ddd;border:1px solid #aaa}
.f-btn{top:199px;width:89px;height:25px;border-radius:4px;color:#fff;font-size:10px;font-weight:700;display:flex;align-items:center;justify-content:center}
.f-search{left:305px;background:linear-gradient(#15405f,#0b2437)}
.f-reset{left:400px;background:linear-gradient(#2a2a2a,#0e0e0e)}
/* results */
.results{left:0;top:628px;width:794px;height:318px;background:var(--light)}
.results-title{left:0;top:36px;width:794px;justify-content:center;font-size:17px}
.table{left:31px;top:71px;width:732px;table-layout:fixed;border-collapse:collapse;background:#fff;border-radius:6px;overflow:hidden;box-shadow:0 0 0 1px #ddd}
.table th{background:var(--blue);color:#fff;font-size:10px;font-weight:700;height:40px;border-right:1px solid rgba(255,255,255,.5)}
.table td{height:33px;font-size:10px;color:#333;border-right:1px solid #ddd;padding:0 7px 0 14px;white-space:nowrap;overflow:hidden}
.table tr:nth-child(odd) td{background:var(--row)}
.table th:last-child,.table td:last-child{border-right:0}
.table td:last-child{padding:0 6px 0 9px}
.c{text-align:center}
.table td.c{padding:0}
/* footer */
.footer{left:0;top:946px;width:794px;height:220px;background:var(--footer)}
.f-brand{left:40px;top:78px;display:flex;align-items:center;gap:10px}
.f-brand .brand-dot{width:50px;height:50px}
.f-brand .brand-name{font-size:30px}
.col-title{top:28px;font-size:11.5px;font-weight:700;color:var(--blue);padding-bottom:6px;border-bottom:1px solid #3a3a3a}
.links{left:276px;top:70px;font-size:8.5px;line-height:14.5px;color:#9a9a9a}
.contact{left:394px;font-size:8.5px;line-height:12.5px;color:#9a9a9a;display:flex;gap:6px;align-items:flex-start}
.contact svg{flex:none}
.qm{left:546px;width:208px;background:var(--footer-field);font-size:7px;color:#aaa;padding:6px 9px}
.qm-submit{left:546px;top:161px;width:72px;height:19px;background:#3a3a3a;color:#fff;font-size:9px;font-weight:700;display:flex;align-items:center;justify-content:center}
.bar{left:0;top:1166px;width:794px;height:16px;background:var(--blue)}
.copy{left:20px;top:2px;font-size:6.5px;font-weight:700;color:#fff}
.social{right:10px;top:1px;display:flex;gap:3px}
.social i{display:block;width:14px;height:14px;border-radius:50%;background:#fff}
</style>
</head>
<body>
<div class="page">

  <header>
    <div class="abs brand"><span class="brand-dot"></span><span class="brand-name">Dr. Lumora</span></div>
    <div class="abs lang">ENGLISH &nbsp;I&nbsp; 普通话 &nbsp;I&nbsp; 中文</div>
    <div class="abs member-note">Already a Member? Login Below</div>
    <div class="abs forgot">Forgot Password</div>
    <div class="abs field-top" style="left:468px;width:98px">Login Email</div>
    <div class="abs field-top" style="left:576px;width:102px">Password</div>
    <div class="abs btn-login">LOGIN</div>
  </header>

  <nav class="abs nav">
    <div class="abs nav-item nav-home" style="left:60px;width:76px">HOME</div>
    <div class="abs nav-item" style="left:146px;width:98px">HEALTH INFO</div>
    <div class="abs nav-sep" style="left:244px"></div>
    <div class="abs nav-item" style="left:244px;width:74px">NEWS</div>
    <div class="abs nav-sep" style="left:318px"></div>
    <div class="abs nav-item" style="left:318px;width:92px">ABOUT US</div>
    <div class="abs nav-sep" style="left:410px"></div>
    <div class="abs nav-item" style="left:410px;width:108px">CONTACT US</div>
    <div class="abs nav-sep" style="left:518px"></div>
    <div class="abs nav-search">
      <svg width="9" height="9" viewBox="0 0 10 10"><circle cx="4" cy="4" r="3" fill="none" stroke="#333" stroke-width="1.4"/><path d="M6.3 6.3L9 9" stroke="#333" stroke-width="1.4"/></svg>SEARCH
    </div>
  </nav>

  <section class="membership">
    <h2 class="abs section-title" style="left:254px;top:158px">
      <svg width="18" height="22" viewBox="0 0 18 22"><path d="M9 1a7 7 0 0 1 7 7c0 5-7 13-7 13S2 13 2 8a7 7 0 0 1 7-7z" fill="none" stroke="var(--blue)" stroke-width="2"/><circle cx="9" cy="8" r="3" fill="var(--blue)"/></svg>
      BECOME A DR. LUMORA MEMBER
    </h2>
    <div class="abs perk" style="left:65px;top:196px">
      <div class="perk-ring"><div class="perk-disc"><svg width="40" height="34" viewBox="0 0 40 34" fill="none" stroke="#fff" stroke-width="2"><rect x="4" y="2" width="32" height="30" rx="2"/><path d="M9 9h22M9 15h10M9 21h10M9 27h22M23 15h8v6h-8z"/></svg></div></div>
      First-Hand Health News
    </div>
    <div class="abs perk" style="left:201px;top:216px">
      <div class="perk-ring"><div class="perk-disc"><svg width="40" height="40" viewBox="0 0 40 40" fill="none" stroke="#fff" stroke-width="2"><circle cx="20" cy="16" r="12"/><path d="M20 9l2.2 4.6 5 .7-3.6 3.5.9 5L20 20.5l-4.5 2.3.9-5-3.6-3.5 5-.7z"/><path d="M12 25l-5 10 6-2 3 5 3-9M28 25l5 10-6-2-3 5-3-9"/></svg></div></div>
      Exclusive Promotions
    </div>
    <div class="abs perk" style="left:336px;top:236px">
      <div class="perk-ring"><div class="perk-disc"><svg width="40" height="40" viewBox="0 0 40 40" fill="none" stroke="#fff" stroke-width="2"><rect x="12" y="6" width="24" height="30" rx="2"/><path d="M18 6V3h12v3M22 15h10M22 22h10M22 29h10"/><path d="M4 14l8-4 8 4v8c0 6-8 10-8 10s-8-4-8-10z" fill="var(--blue)"/><path d="M8 20l3 3 5-6"/></svg></div></div>
      Instant Health Advices
    </div>
    <div class="abs perk" style="left:472px;top:216px">
      <div class="perk-ring"><div class="perk-disc"><svg width="40" height="38" viewBox="0 0 40 38" fill="none" stroke="#fff" stroke-width="2"><rect x="6" y="2" width="28" height="20" rx="1"/><path d="M12 16l6-6 4 4 6-7"/><circle cx="10" cy="28" r="2.5" fill="#fff"/><circle cx="20" cy="28" r="2.5" fill="#fff"/><circle cx="30" cy="28" r="2.5" fill="#fff"/><path d="M5 36c0-3 2-4 5-4s5 1 5 4M15 36c0-3 2-4 5-4s5 1 5 4M25 36c0-3 2-4 5-4s5 1 5 4"/></svg></div></div>
      Free Health<br>Seminars / Talks
    </div>
    <div class="abs perk" style="left:608px;top:196px">
      <div class="perk-ring"><div class="perk-disc" role="img" aria-label="Doctor appointment icon"></div></div>
      Priority Doctor<br>Appointments
    </div>
  </section>

  <section class="abs finder" role="img" aria-label="Lively crowd of people on a city street, tinted blue">
    <h2 class="abs section-title finder-title">
      <svg width="24" height="22" viewBox="0 0 24 22" fill="#fff"><circle cx="8" cy="6" r="4"/><path d="M0 20c0-5 3-8 8-8s8 3 8 8z"/><circle cx="17" cy="15" r="3.5" fill="none" stroke="#fff" stroke-width="1.6"/><path d="M19.5 17.5L23 21" stroke="#fff" stroke-width="1.8"/></svg>
      FIND A DOCTOR
    </h2>
    <div class="abs f-label" style="left:56px;top:95px">Doctor's Name :</div>
    <div class="abs f-input" style="left:136px;top:92px;width:227px"></div>
    <div class="abs f-label" style="left:56px;top:125px">Gender :</div>
    <div class="abs check" style="left:146px;top:125px"><i></i>Male</div>
    <div class="abs check" style="left:197px;top:125px"><i></i>Female</div>
    <div class="abs f-label" style="left:56px;top:155px">Specialism :</div>
    <div class="abs f-input f-select" style="left:136px;top:152px;width:227px"><svg width="10" height="7" viewBox="0 0 10 7"><path d="M1 1l4 4 4-4" fill="none" stroke="#222" stroke-width="1.8"/></svg></div>

    <div class="abs f-label" style="left:432px;top:95px">Symptoms :</div>
    <div class="abs f-input f-select" style="left:512px;top:92px;width:227px"><svg width="10" height="7" viewBox="0 0 10 7"><path d="M1 1l4 4 4-4" fill="none" stroke="#222" stroke-width="1.8"/></svg></div>
    <div class="abs f-label" style="left:432px;top:125px">District :</div>
    <div class="abs f-input f-select" style="left:512px;top:122px;width:227px"><svg width="10" height="7" viewBox="0 0 10 7"><path d="M1 1l4 4 4-4" fill="none" stroke="#222" stroke-width="1.8"/></svg></div>
    <div class="abs f-label" style="left:432px;top:155px">Phone Number :</div>
    <div class="abs f-input" style="left:512px;top:152px;width:227px"></div>

    <div class="abs f-btn f-search">SEARCH</div>
    <div class="abs f-btn f-reset">RESET</div>
  </section>

  <section class="abs results">
    <h2 class="abs section-title results-title">
      <svg width="24" height="22" viewBox="0 0 24 22" fill="var(--blue)"><circle cx="8" cy="6" r="4"/><path d="M0 20c0-5 3-8 8-8s8 3 8 8z"/><circle cx="17" cy="15" r="3.5" fill="none" stroke="var(--blue)" stroke-width="1.6"/><path d="M19.5 17.5L23 21" stroke="var(--blue)" stroke-width="1.8"/></svg>
      SEARCH RESULTS
    </h2>
    <table class="abs table">
      <colgroup><col style="width:194px"><col style="width:64px"><col style="width:122px"><col style="width:82px"><col style="width:108px"><col style="width:78px"><col style="width:84px"></colgroup>
      <tr><th>Name</th><th>Gender</th><th>Specialism</th><th>Hospital</th><th>Address</th><th>District</th><th>Phone</th></tr>
      <tr><td>Tam Wing Kei</td><td class="c"><svg width="14" height="16" viewBox="0 0 14 16" fill="#1a5f9c"><circle cx="7" cy="4" r="3.5"/><path d="M0 16c0-5 3-7 7-7s7 2 7 7z"/></svg></td><td>Cardiology</td><td class="c">Private</td><td>218 Maple Rd</td><td>Kwai Tsing</td><td>555-014-2281</td></tr>
      <tr><td>Lau Siu Man, Mei</td><td class="c"><svg width="14" height="16" viewBox="0 0 14 16" fill="var(--pink)"><circle cx="7" cy="4" r="3.5"/><path d="M0 16c0-5 3-7 7-7s7 2 7 7z"/></svg></td><td>Dentistry</td><td class="c">Private</td><td>6 Orchid Lane</td><td>Kowloon</td><td>555-027-3390</td></tr>
      <tr><td>Ho K L Marcus</td><td class="c"><svg width="14" height="16" viewBox="0 0 14 16" fill="#1a5f9c"><circle cx="7" cy="4" r="3.5"/><path d="M0 16c0-5 3-7 7-7s7 2 7 7z"/></svg></td><td>Endocrinology</td><td class="c">Private</td><td>104 Harbour Vale</td><td>Sai Kung</td><td>555-036-4417</td></tr>
      <tr><td>Fung Yat, Calvin</td><td class="c"><svg width="14" height="16" viewBox="0 0 14 16" fill="#1a5f9c"><circle cx="7" cy="4" r="3.5"/><path d="M0 16c0-5 3-7 7-7s7 2 7 7z"/></svg></td><td>Gastroenterology</td><td class="c">Private</td><td>42 Cedar Rise</td><td>Tai Po</td><td>555-048-5526</td></tr>
      <tr><td>Yip Lai Ching</td><td class="c"><svg width="14" height="16" viewBox="0 0 14 16" fill="var(--pink)"><circle cx="7" cy="4" r="3.5"/><path d="M0 16c0-5 3-7 7-7s7 2 7 7z"/></svg></td><td>General Surgery</td><td class="c">Private</td><td>128 Lantern St</td><td>Wan Chai</td><td>555-059-6634</td></tr>
    </table>
  </section>

  <footer class="abs footer">
    <div class="abs f-brand"><span class="brand-dot"></span><span class="brand-name">Dr. Lumora</span></div>

    <div class="abs col-title" style="left:276px;width:80px">Navigation</div>
    <div class="abs links">Home<br>Health Info<br>News<br>About Us<br>Contact Us</div>

    <div class="abs col-title" style="left:388px;width:130px">Contact Us</div>
    <div class="abs contact" style="top:66px"><svg width="17" height="17" viewBox="0 0 18 18" fill="none" stroke="var(--blue)" stroke-width="1.3"><circle cx="9" cy="9" r="8"/><path d="M9 4a3 3 0 0 1 3 3c0 2.5-3 6-3 6S6 9.5 6 7a3 3 0 0 1 3-3z"/></svg><span>DR LUMORA<br>88 Willow Bay Rd<br>Sunset Point<br>Harbourton</span></div>
    <div class="abs contact" style="top:124px;align-items:center"><svg width="17" height="17" viewBox="0 0 18 18" fill="none" stroke="var(--blue)" stroke-width="1.3"><circle cx="9" cy="9" r="8"/><path d="M6 5l2 2-1 1.5c.7 1.3 1.5 2.1 2.5 2.5L11 10l2 2-1 1.5C9 13 5.5 9.5 5.5 6.5z"/></svg><span>555-014-2281</span></div>
    <div class="abs contact" style="top:149px;align-items:center"><svg width="17" height="17" viewBox="0 0 18 18" fill="none" stroke="var(--blue)" stroke-width="1.3"><circle cx="9" cy="9" r="8"/><rect x="5" y="7.5" width="8" height="5" rx="1"/><path d="M6.5 7.5V5h5v2.5"/></svg><span>555-014-2282</span></div>
    <div class="abs contact" style="top:175px;align-items:center"><svg width="17" height="17" viewBox="0 0 18 18" fill="none" stroke="var(--blue)" stroke-width="1.3"><circle cx="9" cy="9" r="8"/><rect x="4.5" y="6" width="9" height="6.5"/><path d="M4.5 6L9 10l4.5-4"/></svg><span>info@drlumora.com</span></div>

    <div class="abs col-title" style="left:548px;width:216px">Quick Message</div>
    <div class="abs qm" style="top:64px;height:20px">Name</div>
    <div class="abs qm" style="top:88px;height:20px">Email</div>
    <div class="abs qm" style="top:112px;height:45px">Message</div>
    <div class="abs qm-submit">SUBMIT</div>
  </footer>

  <div class="abs bar">
    <div class="abs copy">COPYRIGHT © 2016 DR LUMORA. ALL RIGHTS RESERVED.</div>
    <div class="abs social"><i></i><i></i><i></i></div>
  </div>

</div>
</body>
</html>
```